Brisk Morsels
Business Card and Stationary Design
Brisk Morsels -
Creative Brief
Bright & Fun-filled
Gordon T Welham
Owner
41 Harlow Lane Millbrook Ridge, NJ 08637
Gord.Welham@postmailer.example
www.brisk-morsels.example
Looking for something simple, but eye-catching. Looking for a variety of different fonts/styles/backgrounds to achieve: -Seamless integration with the attached logo. -Backgrounds to enhance the "pop" of the logo. -Professional, but with a hint of fun. The Brisk Morsel will compete in the energy drink/shot industry (e.g. Tan Lynx and Nine Minute Vigor). We differentiate ourselves through superior taste and natural ingredients, creating a more satisfying experience for the energy consumer. Feel free to message me with any questions/concerns/comments.

```html
<!DOCTYPE html>
<html lang="en">
<head>
<meta charset="utf-8">
<title>Brisk Morsels — Business Card</title>
<link rel="stylesheet" href="https://fonts.googleapis.com/css2?family=Oswald:wght@400;500;600&display=swap">
<style>
  :root {
    --stage: #ededed;
    --card-white: #ffffff;
    --orange: #e0895a;
    --orange-text: #e07a3c;
    --brown: #5a3b1c;
    --brown-soft: #6e4a27;
    --dot-grey: #dcdcdc;
  }
  * { margin: 0; padding: 0; box-sizing: border-box; }
  html, body { width: 1200px; height: 871px; overflow: hidden; }
  body {
    background: var(--stage);
    font-family: "Oswald", "Arial Narrow", sans-serif;
    position: relative;
  }
  .card {
    position: absolute;
    overflow: hidden;
    box-shadow: 0 4px 14px rgba(0,0,0,0.18);
  }
  /* Front */
  .card-front {
    left: 48px; top: 101px; width: 504px; height: 331px;
    background: var(--card-white);
  }
  .front-texture {
    position: absolute; right: 0; top: 0; width: 360px; height: 200px;
    background: radial-gradient(ellipse at 75% 25%, var(--dot-grey) 0%, rgba(255,255,255,0) 70%);
    opacity: 0.8;
  }
  .front-swoosh { position: absolute; left: 0; top: 0; }
  .brand-front {
    position: absolute; left: 38px; top: 176px;
    display: flex; align-items: center; gap: 8px;
  }
  .brand-mark {
    width: 24px; height: 24px; border-radius: 50%;
    background: var(--orange);
  }
  .brand-name {
    font-weight: 600; font-size: 30px; line-height: 1;
    color: var(--brown); letter-spacing: 0.3px; white-space: nowrap;
  }
  .contact {
    position: absolute; left: 360px; top: 126px; width: 144px;
    text-align: center;
  }
  .contact-role {
    font-size: 8px; font-weight: 500; letter-spacing: 1px;
    color: var(--orange-text); text-transform: uppercase;
  }
  .contact-name {
    font-size: 17px; font-weight: 600; line-height: 1.1;
    color: var(--orange-text); text-transform: uppercase;
    margin-bottom: 8px; white-space: nowrap;
  }
  .contact-line {
    font-size: 7.5px; font-weight: 500; letter-spacing: 0.8px; line-height: 1.55;
    color: var(--brown-soft); text-transform: uppercase; white-space: nowrap;
  }
  /* Back */
  .card-back {
    left: 566px; top: 456px; width: 567px; height: 343px;
    background: var(--orange);
  }
  .band { position: absolute; left: 0; width: 100%; background: var(--brown); }
  .band-top { top: 0; height: 53px; }
  .band-bottom { bottom: 0; height: 46px; }
  .brand-back {
    position: absolute; left: 0; top: 128px; width: 100%;
    display: flex; justify-content: center; align-items: center; gap: 7px;
  }
  .brand-back .brand-mark { width: 20px; height: 20px; background: var(--brown); }
  .brand-back .brand-name { font-size: 26px; color: var(--brown); }
  .web {
    position: absolute; left: 0; top: 246px; width: 100%;
    text-align: center; font-size: 10px; font-weight: 500;
    letter-spacing: 2.5px; color: #fff; text-transform: uppercase;
  }
</style>
</head>
<body>
  <section class="card card-front">
    <div class="front-texture" role="img" aria-label="Soft grey halftone dot texture"></div>
    <svg class="front-swoosh" width="504" height="331" viewBox="0 0 504 331">
      <path fill="var(--orange)" d="M18,14 C220,18 345,80 345,165 C345,240 270,300 150,331 L118,331 C235,295 305,235 300,170 C292,90 190,35 18,14 Z"/>
      <path fill="var(--brown)" d="M14,26 C190,42 300,100 312,175 C320,250 230,305 100,331 L68,331 C190,300 272,245 268,180 C262,105 170,50 14,26 Z"/>
    </svg>
    <div class="brand-front">
      <span class="brand-mark"></span>
      <span class="brand-name">Brisk Morsels</span>
    </div>
    <div class="contact">
      <p class="contact-role">Owner</p>
      <p class="contact-name">Gordon T Welham</p>
      <p class="contact-line">41 Harlow Lane</p>
      <p class="contact-line">Millbrook Ridge, NJ 08637</p>
      <p class="contact-line">(555) 014-2290</p>
      <p class="contact-line">Gord.Welham@postmailer.example</p>
    </div>
  </section>

  <section class="card card-back">
    <div class="band band-top"></div>
    <div class="brand-back">
      <span class="brand-mark"></span>
      <span class="brand-name">Brisk Morsels</span>
    </div>
    <p class="web">www.brisk-morsels.example</p>
    <div class="band band-bottom"></div>
  </section>
</body>
</html>
```